Awesome ecommerce store banner needed!

We need a sharp, clear, strong banner for one of our subcategory pages on http://www.brixmolt.com
We'd like to incorporate the following image. We'd like the background to be gray or black. We are replacing the Wireless Intercoms banner that is orange (we hate it).
WE do like our other banners, however, so please use them as reference:
SIze: 980 x 380
Two raw images of the intercom we'd like you to encorporate have been included. Choose one or the other depending on what you think would be best. If using the single angle, please duplicate it. We want two intercoms in the banner
Simple and Clean is key:
Text: Wireless Intercoms
Text Color: Can be white/off gray
Text Style: Please keep it clean in line with the website
Background: Black/gray/white

```html
<!DOCTYPE html>
<html lang="en">
<head>
<meta charset="utf-8">
<title>Brixmolt – Wireless Intercom Systems</title>
<link rel="stylesheet" href="https://fonts.googleapis.com/css2?family=Open+Sans:wdth,wght@75..100,300..800&display=swap">
<style>
:root{
  --orange:#e87722;
  --orange-red:#d9411e;
  --ink:#2b2b2b;
  --text:#333333;
  --muted:#666666;
  --nav-dark:#2e2e2e;
  --nav-light:#4a4a4a;
  --banner:#1c1c1c;
  --white:#ffffff;
  --card-line:#e2e2e2;
  --unit-silver:#b9b9b9;
  --unit-dark:#2a2a2a;
}
*{margin:0;padding:0;box-sizing:border-box}
html,body{width:1200px;height:895px;overflow:hidden;background:var(--white)}
body{font-family:"Open Sans",Arial,sans-serif;color:var(--text);position:relative}

.site-header{position:absolute;left:0;top:0;width:1200px;height:117px}
.brand{position:absolute;left:34px;top:30px;display:flex;align-items:center;gap:12px}
.brand-dot{width:66px;height:66px;border-radius:50%;background:var(--orange)}
.brand-name{font-weight:800;font-size:56px;letter-spacing:-2px;color:var(--ink);line-height:1}
.account-links{position:absolute;right:26px;top:15px;display:flex;gap:24px;font-size:14px;color:var(--ink);align-items:center}
.cart{display:flex;align-items:center;gap:5px}
.contact{position:absolute;right:28px;top:50px;text-align:right}
.contact-phone{font-stretch:75%;font-weight:700;font-size:23px;color:var(--muted);letter-spacing:-.2px}
.contact-hours{font-size:14px;color:var(--muted);margin-top:2px}

.main-nav{position:absolute;left:26px;top:117px;width:1148px;height:41px;
  background:linear-gradient(var(--nav-light),var(--nav-dark));display:flex;align-items:center}
.nav-item{color:var(--white);font-size:18px;font-weight:500;padding:0 29px;height:41px;line-height:41px;border-right:1px solid #1a1a1a}
.search{position:absolute;right:26px;top:6px;display:flex;align-items:center}
.search-field{width:295px;height:27px;background:#3a3a3a;color:#cfcfcf;font-size:14px;line-height:27px;padding-left:8px}
.search-icon{margin-left:8px}

.promo-bar{position:absolute;left:26px;top:158px;width:1148px;height:36px;background:var(--orange);
  display:flex;justify-content:center;align-items:center;gap:38px;color:var(--white);font-weight:600;font-size:16px}
.promo-bar .sep{width:8px;height:8px;border-radius:50%;background:#111}

.hero{position:absolute;left:26px;top:205px;width:1148px;height:351px;
  background:radial-gradient(ellipse at 40% 45%,#3a3a3a 0%,#262626 45%,var(--banner) 100%);overflow:hidden}
.hero-unit{position:absolute;border-radius:28px}
.hero-unit.back{left:77px;top:90px;width:300px;height:160px;
  background:linear-gradient(100deg,#6d6d6d 0%,#a8a8a8 40%,#5a5a5a 70%,#222 100%)}
.hero-unit.front{left:99px;top:185px;width:373px;height:166px;
  background:linear-gradient(100deg,#7a7a7a 0%,#c2c2c2 40%,#6a6a6a 65%,#1e1e1e 100%)}
.hero-title{position:absolute;left:587px;top:48px;font-weight:800;font-size:90px;font-stretch:90%;
  line-height:72px;letter-spacing:-2px;text-transform:uppercase}
.hero-title .line-1{color:var(--orange);display:block}
.hero-title .line-2{color:var(--white);display:block}

.listing-head{position:absolute;left:26px;top:570px;width:1148px;display:flex;justify-content:space-between;align-items:center}
.listing-title{font-size:27px;font-weight:400;color:#222}
.sort{font-size:14px;color:var(--text);display:flex;align-items:center;gap:6px}
.sort-select{width:173px;height:22px;border:1px solid #999;font-size:13px;padding-left:4px;line-height:20px;position:relative}
.sort-select::after{content:"";position:absolute;right:7px;top:7px;border:4px solid transparent;border-top:6px solid #222}

.product{position:absolute;top:640px;height:260px;border:1px solid var(--card-line);border-bottom:none;background:var(--white)}
.product-flag{position:absolute;left:-1px;top:-1px;width:145px;height:5px;background:var(--orange)}
.product-flag.sale{background:var(--orange-red)}
.product-tab{position:absolute;left:5px;top:4px;width:140px;height:14px;background:var(--orange);clip-path:polygon(0 0,100% 0,95% 100%,0 100%)}
.product-tab.sale{background:var(--orange-red)}
.product-photo{position:absolute;left:5px;top:19px;right:5px;height:228px}
.product-photo.studio{background:linear-gradient(#f2f2f2,#e6e6e6)}
.item{position:absolute;border-radius:14px}
.item.silver{background:linear-gradient(110deg,#9c9c9c,#d8d8d8 45%,#3a3a3a 75%,#222)}
.item.dark{background:linear-gradient(160deg,#3c3c3c,#1a1a1a)}
.item.pale{background:linear-gradient(160deg,#e8e8e8,#b5b5b5)}
.p1{left:34px;width:265px}
.p2{left:325px;width:260px}
.p3{left:606px;width:265px}
.p4{left:892px;width:265px}
</style>
</head>
<body>
<header class="site-header">
  <div class="brand"><span class="brand-dot"></span><span class="brand-name">Brixmolt</span></div>
  <nav class="account-links">
    <span>Sign in or Create an account</span>
    <span>My Account</span>
    <span>Order Status</span>
    <span class="cart"><svg width="18" height="15" viewBox="0 0 18 15"><path d="M1 1h3l2 9h9l2-7H5" fill="none" stroke="#e87722" stroke-width="2"/><circle cx="7" cy="13" r="1.5" fill="#e87722"/><circle cx="14" cy="13" r="1.5" fill="#e87722"/></svg>View Cart</span>
  </nav>
  <div class="contact">
    <div class="contact-phone">Call Us: 1-888-555-0142</div>
    <div class="contact-hours">Monday-Friday, 7am-3pm PST</div>
  </div>
</header>

<nav class="main-nav">
  <span class="nav-item">SHOP GADGETS</span>
  <span class="nav-item">TOP SELLERS</span>
  <span class="nav-item">ON SALE</span>
  <div class="search">
    <div class="search-field">Search by keyword or item #</div>
    <svg class="search-icon" width="22" height="22" viewBox="0 0 22 22"><circle cx="13" cy="9" r="6.5" fill="none" stroke="#cfcfcf" stroke-width="2"/><path d="M8 14l-6 6" stroke="#cfcfcf" stroke-width="2.5"/></svg>
  </div>
</nav>

<div class="promo-bar">
  <span>Expert Advice &amp; Customer Service</span><span class="sep"></span>
  <span>Same-Day Shipping for Most Orders</span><span class="sep"></span>
  <span>30-Day Money Back Guarantee</span>
</div>

<section class="hero">
  <div class="hero-unit back" role="img" aria-label="Silver and black wireless intercom unit with antenna, rear"></div>
  <div class="hero-unit front" role="img" aria-label="Silver and black wireless intercom unit with antenna, front"></div>
  <h1 class="hero-title"><span class="line-1">Wireless</span><span class="line-2">Intercoms</span></h1>
</section>

<div class="listing-head">
  <h2 class="listing-title">Wireless Intercom Systems</h2>
  <div class="sort">Sort by: <div class="sort-select">Featured Items</div></div>
</div>

<article class="product p1"><span class="product-flag"></span><span class="product-tab"></span>
  <div class="product-photo studio">
    <div class="item silver" style="left:18px;top:70px;width:140px;height:80px" role="img" aria-label="Silver intercom unit"></div>
    <div class="item silver" style="left:85px;top:120px;width:150px;height:88px" role="img" aria-label="Second silver intercom unit"></div>
  </div></article>
<article class="product p2">
  <div class="product-photo">
    <div class="item dark" style="left:82px;top:30px;width:84px;height:160px;border-radius:40px" role="img" aria-label="Black door intercom station"></div>
  </div></article>
<article class="product p3"><span class="product-flag sale"></span><span class="product-tab sale"></span>
  <div class="product-photo">
    <div class="item pale" style="left:6px;top:30px;width:70px;height:140px;border-radius:30px" role="img" aria-label="White door intercom station"></div>
    <div class="item silver" style="left:90px;top:110px;width:150px;height:80px" role="img" aria-label="Silver intercom base unit"></div>
  </div></article>
<article class="product p4"><span class="product-flag"></span><span class="product-tab"></span>
  <div class="product-photo">
    <div class="item dark" style="left:10px;top:110px;width:110px;height:80px;border-radius:24px" role="img" aria-label="Black intercom unit with antenna"></div>
    <div class="item dark" style="left:130px;top:110px;width:110px;height:80px;border-radius:24px" role="img" aria-label="Second black intercom unit with antenna"></div>
  </div></article>
</body>
</html>
```